Website Header Development

I am after a redesign of the Header of a website www.kaltroweb.com.au.
This project is for the header only, and should fit in with the rest of the site
Target Market(s)
Business
Requirements
Should not have
- Over the top. Keep it simple

```html
<!DOCTYPE html>
<html lang="en">
<head>
<meta charset="utf-8">
<title>Kaltro Energy – Resource Efficiency</title>
<link rel="stylesheet" href="https://fonts.googleapis.com/css2?family=Alegreya:wght@700&family=Alegreya+Sans:wght@400;500;700&display=swap">
<style>
  :root {
    --page-bg: #f9f9f9;
    --content-bg: #ffffff;
    --sky-top: #c9dcf0;
    --sky-bottom: #e9f1f9;
    --nav-green: #1b7a3b;
    --nav-green-light: #3a8d43;
    --brand-blue: #23378f;
    --headline-navy: #0d1f87;
    --sidebar-blue: #234291;
    --text: #1c1c1c;
    --muted: #9a9a9a;
    --border: #cfcfcf;
    --photo-light: #eef0f2;
    --photo-mid: #d4d9de;
  }
  * { box-sizing: border-box; margin: 0; padding: 0; }
  html, body { width: 1200px; height: 472px; overflow: hidden; background: var(--page-bg); }
  body { position: relative; font-family: "Alegreya Sans", sans-serif; color: var(--text); }

  .site { position: absolute; left: 142px; top: 0; width: 916px; height: 472px; background: var(--content-bg); }

  .masthead {
    position: absolute; left: 0; top: 0; width: 916px; height: 105px;
    background: linear-gradient(180deg, var(--sky-top) 0%, var(--sky-bottom) 78%, #f4f4f4 88%, #dedede 100%);
  }
  .brand {
    position: absolute; left: 0; top: 42px; width: 916px; text-align: center;
    font-family: "Alegreya Sans", sans-serif; font-weight: 500; font-size: 31px;
    color: var(--brand-blue); letter-spacing: 0.5px;
  }
  .brand-mark {
    display: inline-block; width: 14px; height: 14px; border-radius: 50%;
    background: var(--brand-blue); margin-right: 8px; vertical-align: 4px;
  }

  .main-nav {
    position: absolute; left: 0; top: 105px; width: 916px; height: 49px;
    background: var(--nav-green); overflow: hidden;
  }
  .main-nav svg { position: absolute; left: 0; top: 0; }
  .nav-item {
    position: absolute; color: #fff; font-size: 12px; font-weight: 500; top: 13px; white-space: nowrap;
  }
  .nav-item.is-feature { font-size: 14px; font-weight: 700; top: 18px; }

  .headline {
    position: absolute; left: 55px; top: 180px; width: 530px; text-align: center;
    font-family: "Alegreya", serif; font-weight: 700; font-size: 23px; color: var(--headline-navy);
    letter-spacing: 0.3px;
  }
  .intro { position: absolute; left: 55px; top: 226px; width: 190px; font-size: 14px; line-height: 23px; }
  .intro p { margin-bottom: 23px; }

  .feature-photo {
    position: absolute; left: 264px; top: 238px; width: 320px; height: 213px;
    background: radial-gradient(ellipse at 60% 45%, var(--photo-mid) 0%, var(--photo-light) 70%);
  }

  .search {
    position: absolute; left: 674px; top: 155px; width: 169px; height: 28px;
    border: 1px solid var(--border); border-radius: 2px; background: #fff;
    font-family: Arial, sans-serif; font-size: 13px; color: var(--muted);
    padding: 6px 0 0 26px;
  }
  .search svg { position: absolute; left: 8px; top: 7px; }

  .newsletter-title {
    position: absolute; left: 674px; top: 216px; width: 180px;
    font-family: "Alegreya", serif; font-weight: 700; font-size: 19px; line-height: 28px;
    letter-spacing: 2px; color: var(--sidebar-blue);
  }
  .newsletter-copy {
    position: absolute; left: 674px; width: 180px; font-size: 9.5px; font-weight: 700; line-height: 23px;
  }
  .newsletter-field {
    position: absolute; left: 674px; top: 392px; width: 168px; height: 30px;
    border: 1px solid var(--border); background: #fff;
  }
</style>
</head>
<body>
  <div class="site">
    <header class="masthead" role="img" aria-label="Soft blue sky with light clouds">
      <div class="brand"><span class="brand-mark"></span>Kaltro Energy</div>
    </header>

    <nav class="main-nav">
      <svg width="916" height="49" aria-hidden="true">
        <polygon points="50,0 825,0 870,49 20,49" fill="var(--nav-green-light)"/>
      </svg>
      <span class="nav-item is-feature" style="left:77px">Home</span>
      <span class="nav-item" style="left:146px">About Us</span>
      <span class="nav-item" style="left:219px">Services</span>
      <span class="nav-item" style="left:285px">Projects and Case Studies</span>
      <span class="nav-item is-feature" style="left:434px">Financial Information</span>
      <span class="nav-item" style="left:596px">News</span>
      <span class="nav-item" style="left:651px">Contact</span>
    </nav>

    <h1 class="headline">Resource Efficiency – Sustainable Solutions</h1>

    <div class="intro">
      <p>Is your business performing as well as your competitors?</p>
      <p>Are your fixed costs comparable to industry leaders?</p>
      <p>Is your business becoming less profitable with increased energy, waste and water prices?</p>
      <p>Do you wish to reduce your</p>
    </div>

    <div class="feature-photo" role="img" aria-label="Businessman holding up puzzle pieces labelled Solution"></div>

    <div class="search">
      <svg width="13" height="14" viewBox="0 0 13 14" aria-hidden="true">
        <circle cx="7.5" cy="5.5" r="4" fill="none" stroke="#8a8a8a" stroke-width="2"/>
        <line x1="4.5" y1="8.5" x2="1" y2="13" stroke="#8a8a8a" stroke-width="2.5"/>
      </svg>
      Search
    </div>

    <h2 class="newsletter-title">Kaltro Energy Newsletter</h2>
    <p class="newsletter-copy" style="top:316px">Would you like to receive our regular monthly Newsletter? Please fill in your Name:</p>
    <div class="newsletter-field"></div>
    <p class="newsletter-copy" style="top:435px">Let us know your email address so we can send the Newsletter directly to</p>
  </div>
</body>
</html>
```